Luxury Candle Startup Needs Modern Packaging Box & Matching Label Design

We are Lunavale, a luxury candle company about to launch in Australia and we need a box packaging design that is modern, minimalist, and feminine. Our target audience are females, mostly mothers, within the age range of 25-45 who are looking for high quality, handmade luxurious products. Our company is going to have a large social media presence with new mothers as we are going to show our journey with starting a business whilst on maternity leave. We would like the arch shape incorporated into the box packaging as it is beautiful and symbolises moving into a new phase in life which really represents the brand. We would like for the packaging box to be a simple white box with a sleeve insert over the box with the design to make printing easier. Our colour inspiration are very earthy colours and would like the sleeve colour to be easily changed according to the scent. For example dusky rose coloured sleeve for rose patchouli and amber scent, light coffee coloured sleeve for coffee bean cacao scent etc. Please see uploaded files for inspiration, our logo, and the type of candle jars used.
The box dimensions are:
External Dimension: 95mmW x 95mmL x 116mmH
We look forward to seeing your amazing designs!

```html
<!DOCTYPE html>
<html lang="en">
<head>
<meta charset="utf-8">
<title>Lunavale – Coffee Bean Cacao Candle Box</title>
<link rel="stylesheet" href="https://fonts.googleapis.com/css2?family=Cormorant+Garamond:wght@500&family=Kaushan+Script&family=Roboto+Condensed:wght@400&display=swap">
<style>
  :root {
    --page: #f4f4f2;
    --box-white: #ececec;
    --box-edge: #dcdcdc;
    --sleeve-light: #c99a78;
    --sleeve: #b07f5c;
    --sleeve-dark: #9a6d4f;
    --ink: #2a211c;
    --label-white: #f7f7f5;
  }
  * { margin: 0; padding: 0; box-sizing: border-box; }
  html, body {
    width: 1200px; height: 1200px; overflow: hidden;
    background: var(--page);
  }
  .box-face {
    position: absolute;
    left: 280px; top: 209px;
    width: 640px; height: 782px;
    background: var(--box-white);
    border: 1px solid var(--box-edge);
  }
  .sleeve {
    position: absolute;
    left: 150px; top: 0;
    width: 340px; height: 100%;
    background: linear-gradient(160deg, var(--sleeve-light) 0%, var(--sleeve) 45%, var(--sleeve-dark) 100%);
  }
  .brand-tab {
    position: absolute;
    left: 80px; top: 0;
    width: 180px; height: 130px;
    background: var(--label-white);
    display: flex; align-items: center; justify-content: center;
  }
  .brand-name {
    font-family: "Cormorant Garamond", serif;
    font-weight: 500;
    font-size: 24px;
    letter-spacing: 2px;
    color: var(--ink);
    text-transform: uppercase;
    white-space: nowrap;
  }
  .wreath {
    position: absolute;
    left: 0; top: 235px;
    width: 340px; height: 470px;
    border-radius: 50%;
    background: radial-gradient(ellipse at center, transparent 38%, rgba(140,101,72,0.55) 52%, rgba(140,101,72,0.35) 66%, transparent 74%);
  }
  .scent-label {
    position: absolute;
    left: 30px; top: 370px;
    width: 280px;
    text-align: center;
    color: var(--ink);
  }
  .scent-name {
    font-family: "Kaushan Script", cursive;
    font-weight: 400;
    font-size: 30px;
    line-height: 1.1;
    transform: rotate(-4deg);
  }
  .scent-tagline {
    font-family: "Roboto Condensed", sans-serif;
    font-size: 15px;
    margin: 20px auto 6px;
    padding-bottom: 4px;
    width: 190px;
    border-bottom: 1px solid var(--ink);
  }
  .ingredients {
    font-family: "Roboto Condensed", sans-serif;
    font-size: 14px;
    line-height: 1.45;
    border: 1.5px solid var(--ink);
    border-radius: 6px;
    padding: 6px 12px;
    margin: 0 24px;
  }
  .ingredients-line {
    display: block;
    text-align: justify;
    text-align-last: justify;
    white-space: nowrap;
  }
</style>
</head>
<body>
  <main class="box-face">
    <section class="sleeve">
      <div class="brand-tab"><span class="brand-name">Lunavale</span></div>
      <div class="wreath" role="img" aria-label="Hand-drawn botanical wreath of leaves and coffee sprigs framing the scent label"></div>
      <div class="scent-label">
        <h1 class="scent-name">Coffee Bean Cacao</h1>
        <p class="scent-tagline">Homemade Candle scents</p>
        <p class="ingredients">
          <span class="ingredients-line">Ingredients: ipsum dolor sit amet,</span>
          <span class="ingredients-line">consectetuer adipiscing elit, sed</span>
          <span class="ingredients-line">diam nonummy nibh euismod</span>
          <span class="ingredients-line">tincidunt ut laoreet dolore magna</span>
        </p>
      </div>
    </section>
  </main>
</body>
</html>
```